Coral Ridge Networks Ltd

I need a website that is an informational only. We are a construction business building telecommunications sites. Seeing how our company is Coral Ridge the color blue might want to be incorporated in the color scheme.
I can provide more picture of towers and wireless communications if needed.
current website www.coralridgenet.ca

Industry/Entity Type

Wireless Telecommunications, Construction

Coding

Coded - Design and coding required

Number of Pages Required

2 page

Font styles to use
Sans Serif

Colors

Designer to choose colors to be used in the design.

```html
<!DOCTYPE html>
<html lang="en">
<head>
<meta charset="utf-8">
<title>Coral Ridge Networks Ltd</title>
<link href="https://fonts.googleapis.com/css2?family=Montserrat:wght@400;500;600;700&display=swap" rel="stylesheet">
<style>
:root{
  --ink:#111;
  --text:#444;
  --muted:#8a8f99;
  --accent:#0b57b4;
  --band:#2f3f93;
  --hero-box:rgba(44,62,168,.86);
  --footer:#0b3672;
  --tint:#f7f9fe;
  --line:#d5d9e2;
  --btn-a:#4e9bd8;
  --btn-b:#2a4fa6;
}
*{box-sizing:border-box;margin:0;padding:0}
html,body{width:1200px;height:2804px;overflow:hidden}
body{position:relative;background:#fff;font-family:'Montserrat',sans-serif;color:var(--ink)}
.abs{position:absolute}
.accent{color:var(--accent)}

/* header */
.brand{left:109px;top:24px;font-size:30px;font-weight:600;color:var(--accent);display:flex;align-items:center;gap:8px}
.brand-dot{width:14px;height:14px;background:var(--accent);border-radius:50%}
.nav{top:36px;font-size:16px;color:#222}
.nav.active{color:var(--accent);font-weight:500}
.btn-contact{left:790px;top:27px;width:102px;height:35px;background:linear-gradient(90deg,var(--btn-a),var(--btn-b));color:#fff;font-size:16px;display:flex;align-items:center;justify-content:center;border-radius:2px}
.head-phone{left:933px;top:36px;font-size:14px;font-weight:600;color:var(--footer);display:flex;align-items:center;gap:6px}

/* hero */
.hero{left:0;top:89px;width:1200px;height:550px;background:linear-gradient(180deg,#2d4f9a 0%,#5b7bb4 35%,#8a9bb0 55%,#7b7f86 100%)}
.hero-box{left:110px;top:410px;width:497px;height:150px;background:var(--hero-box)}
.hero-rule{left:138px;top:458px;width:2px;height:128px;background:#fff}
.hero-title{left:164px;top:436px;color:#fff;font-size:27px;font-weight:700;line-height:32px}

/* about */
.about-photo{left:128px;top:754px;width:455px;height:288px;background:linear-gradient(135deg,#b9bfc6,#5d6470 60%,#3d434c)}
.badge{left:488px;top:763px;width:87px;height:107px;border:1px solid rgba(255,255,255,.7);background:rgba(20,24,30,.75);color:#fff;text-align:center}
.badge b{display:block;font-size:48px;font-weight:700;line-height:50px;margin-top:10px}
.badge span{display:block;font-size:17px;font-weight:600}
.badge small{display:block;font-size:7px;letter-spacing:1px;margin-top:4px}
.about-title{left:632px;top:806px;font-size:32px;font-weight:500}
.about-copy{left:632px;top:862px;width:355px;font-size:13.5px;line-height:21px;color:var(--text)}
.about-copy p+p{margin-top:16px}

/* call band */
.tint{left:0;top:1205px;width:1181px;height:680px;background:var(--tint)}
.callband{left:128px;top:1129px;width:943px;height:180px;background:var(--band);color:#fff;text-align:center}
.callband h3{font-size:20px;font-weight:500;line-height:28px;margin-top:42px}
.callband p{font-size:14px;margin-top:14px}
.callband .num{font-size:19px;font-weight:600;margin-top:6px;display:flex;justify-content:center;align-items:center;gap:10px}

/* testimonials */
.testi-title{left:0;top:1420px;width:1200px;text-align:center;font-size:32px;font-weight:600;line-height:37px}
.card{top:1543px;width:296px;height:236px;background:#fff;text-align:center;padding:24px 30px 0;box-shadow:0 4px 18px rgba(30,50,100,.06)}
.card .q{font-size:60px;font-weight:700;line-height:40px;height:40px;color:#7c8aa8}
.card p{font-size:12.3px;line-height:18.5px;color:#9aa0a9;margin-top:14px}
.card .who{font-size:13.5px;font-weight:500;color:#888;margin-top:14px}
.card.focus .q{color:#1d2d55}
.card.focus p{color:#222}
.card.focus .who{color:var(--footer)}
.arrow{top:1643px;width:43px;height:43px;background:#fff;border:1px solid #e2e6ee;display:flex;align-items:center;justify-content:center}

/* map & form */
.map{left:0;top:1884px;width:1200px;height:416px;background:linear-gradient(160deg,#e6ebe4,#dfe3e7 50%,#b9d3e6)}
.map-pin{left:633px;top:1965px;width:130px;height:86px;background:#fff;border-radius:6px;box-shadow:0 3px 10px rgba(0,0,0,.15);display:flex;align-items:center;justify-content:center;font-size:18px;font-weight:600;color:var(--accent)}
.footer{left:0;top:2300px;width:1200px;height:504px;background:var(--footer)}
.form{left:129px;top:2131px;width:940px;height:414px;background:#fff}
.form h2{position:absolute;left:0;top:52px;width:100%;text-align:center;font-size:31px;font-weight:600}
.field{position:absolute;height:42px;border:1px solid var(--line);font-size:13.5px;color:#777;padding:0 19px;display:flex;align-items:center;justify-content:space-between}
.field.area{align-items:flex-start;padding-top:14px;height:86px}
.send{position:absolute;left:406px;top:328px;width:131px;height:48px;background:linear-gradient(90deg,var(--btn-a),var(--btn-b));color:#fff;font-size:16px;display:flex;align-items:center;justify-content:center}

/* footer */
.foot-brand{left:129px;top:2602px;width:166px;height:110px;background:#fff;border-radius:6px;display:flex;align-items:center;justify-content:center;font-size:19px;font-weight:600;color:var(--accent)}
.foot-col{top:2601px;color:#fff}
.foot-col h4{font-size:18px;font-weight:600;margin-bottom:16px}
.foot-col li{list-style:none;font-size:13px;color:#d4dcec;line-height:25px}
.foot-col .row{display:flex;gap:8px;align-items:flex-start;line-height:15px;margin-bottom:12px}
</style>
</head>
<body>

<header>
  <div class="abs brand"><span class="brand-dot"></span>Coral Ridge</div>
  <a class="abs nav active" style="left:600px">Home</a>
  <a class="abs nav" style="left:688px">Services</a>
  <a class="abs btn-contact">Contact</a>
  <div class="abs head-phone">
    <svg width="15" height="15" viewBox="0 0 24 24"><path fill="#0b3672" d="M6.6 10.8a15 15 0 006.6 6.6l2.2-2.2c.3-.3.7-.4 1-.2 1.1.4 2.3.6 3.6.6.6 0 1 .4 1 1V20c0 .6-.4 1-1 1A17 17 0 013 4c0-.6.4-1 1-1h3.5c.6 0 1 .4 1 1 0 1.3.2 2.5.6 3.6.1.3 0 .7-.2 1z"/></svg>
    1-604-555-0192
  </div>
</header>

<section>
  <div class="abs hero" role="img" aria-label="Rooftop telecommunications equipment with mountains and city in the background"></div>
  <div class="abs hero-box"></div>
  <div class="abs hero-rule"></div>
  <h1 class="abs hero-title">We Are A<br>Construction Business Building<br>Telecommunications Sites</h1>
</section>

<section>
  <div class="abs about-photo" role="img" aria-label="Technician working on a telecommunications tower"></div>
  <div class="abs badge"><b>15</b><span>YEARS</span><small>EXPERIENCE</small></div>
  <h2 class="abs about-title">About <span class="accent">Coral Ridge</span></h2>
  <div class="abs about-copy">
    <p><span class="accent">At Coral Ridge Ltd</span>, we are dedicated to providing our customers with friendly professional service. We value your business. We have made it our mission to provide reliable products and services in our customer-driven approach.</p>
    <p>Our courteous, professional team is able to support a range of services to meet your requirements.</p>
  </div>
</section>

<div class="abs tint"></div>

<section class="abs callband">
  <h3>TO LEARN MORE ABOUT CORAL RIDGE LTD, AND THE<br>PRODUCTS AND SERVICES WE CAN OFFER</h3>
  <p>please call us at</p>
  <div class="num">
    <svg width="22" height="22" viewBox="0 0 24 24"><path fill="#fff" d="M6.6 10.8a15 15 0 006.6 6.6l2.2-2.2c.3-.3.7-.4 1-.2 1.1.4 2.3.6 3.6.6.6 0 1 .4 1 1V20c0 .6-.4 1-1 1A17 17 0 013 4c0-.6.4-1 1-1h3.5c.6 0 1 .4 1 1 0 1.3.2 2.5.6 3.6.1.3 0 .7-.2 1z"/></svg>
    1-604-555-0192
  </div>
</section>

<section>
  <h2 class="abs testi-title">What Our Customers Saying<br>About <span class="accent">Coral Ridge</span></h2>
  <div class="abs arrow" style="left:109px"><svg width="20" height="20" viewBox="0 0 24 24"><path d="M20 12H5M11 5l-7 7 7 7" stroke="#0b57b4" stroke-width="2.2" fill="none"/></svg></div>
  <div class="abs arrow" style="left:1048px"><svg width="20" height="20" viewBox="0 0 24 24"><path d="M4 12h15M13 5l7 7-7 7" stroke="#0b57b4" stroke-width="2.2" fill="none"/></svg></div>
  <article class="abs card" style="left:130px"><div class="q">&ldquo;</div><p>Lorem ipsum dolor sit amet, consectetur adipiscing elit. Netus egestas egestas pellentesque semper. Nisl, et sem mollis arcu et duis eu nam. Ut adipiscing gravida duis faucibus neque, fermentum ultricies.</p><div class="who">&ndash;&ndash; Dana Whitfield</div></article>
  <article class="abs card focus" style="left:452px"><div class="q">&ldquo;</div><p>Lorem ipsum dolor sit amet, consectetur adipiscing elit. Netus egestas egestas pellentesque semper. Nisl, et sem mollis arcu et duis eu nam. Ut adipiscing gravida duis faucibus neque, fermentum ultricies.</p><div class="who">&ndash;&ndash; Dana Whitfield</div></article>
  <article class="abs card" style="left:774px"><div class="q">&ldquo;</div><p>Lorem ipsum dolor sit amet, consectetur adipiscing elit. Netus egestas egestas pellentesque semper. Nisl, et sem mollis arcu et duis eu nam. Ut adipiscing gravida duis faucibus neque, fermentum ultricies.</p><div class="who">&ndash;&ndash; Dana Whitfield</div></article>
</section>

<div class="abs map" role="img" aria-label="Street map showing the office location near the river"></div>
<div class="abs map-pin">Coral Ridge</div>
<footer class="abs footer"></footer>

<section class="abs form">
  <h2>How Can <span class="accent">Coral Ridge</span> Help You?</h2>
  <div class="field" style="left:42px;top:109px;width:420px">Your Name</div>
  <div class="field" style="left:479px;top:109px;width:420px">Your Phone</div>
  <div class="field" style="left:42px;top:167px;width:420px">Your Email</div>
  <div class="field" style="left:479px;top:167px;width:420px">Service you need<svg width="14" height="14" viewBox="0 0 24 24"><path d="M5 9l7 7 7-7" stroke="#555" stroke-width="2" fill="none"/></svg></div>
  <div class="field area" style="left:42px;top:226px;width:857px">Please tell us your feedback</div>
  <div class="send">Send Us</div>
</section>

<div class="abs foot-brand">Coral Ridge</div>
<div class="abs foot-col" style="left:474px"><h4>Privacy</h4><ul><li>Privacy Policy</li><li>Get In Touch</li></ul></div>
<div class="abs foot-col" style="left:666px"><h4>Social Media</h4><ul><li>Social Feed</li><li>Photo Stream</li><li>Pro Network</li><li>Microblog</li></ul></div>
<div class="abs foot-col" style="left:887px;width:190px"><h4>Contact Us</h4>
  <ul>
    <li class="row"><svg width="12" height="14" viewBox="0 0 24 24"><path d="M12 22s7-7 7-12a7 7 0 00-14 0c0 5 7 12 7 12z" stroke="#d4dcec" stroke-width="2" fill="none"/><circle cx="12" cy="10" r="2.5" stroke="#d4dcec" stroke-width="2" fill="none"/></svg><span>4150 Harbour Line Rd, Surrey, BC V3X1K7</span></li>
    <li class="row"><svg width="12" height="12" viewBox="0 0 24 24"><path d="M6.6 10.8a15 15 0 006.6 6.6l2.2-2.2c.3-.3.7-.4 1-.2 1.1.4 2.3.6 3.6.6.6 0 1 .4 1 1V20c0 .6-.4 1-1 1A17 17 0 013 4c0-.6.4-1 1-1h3.5c.6 0 1 .4 1 1 0 1.3.2 2.5.6 3.6.1.3 0 .7-.2 1z" stroke="#d4dcec" stroke-width="2" fill="none"/></svg><span>1-604-555-0192</span></li>
    <li class="row"><svg width="12" height="12" viewBox="0 0 24 24"><rect x="3" y="5" width="18" height="14" stroke="#d4dcec" stroke-width="2" fill="none"/><path d="M3 6l9 7 9-7" stroke="#d4dcec" stroke-width="2" fill="none"/></svg><span>info@coralridgenet.ca</span></li>
  </ul>
</div>

</body>
</html>
```